Business Card Design

New business card design

Target Market(s)

Residential & Commercial Property Managers

Industry/Entity Type

Plumbing Services

Contact Information for Business Card

Name - Owen Tredgold, title - Director, Phone Number - 0431 862 507, email - owen@rvb-plumbing.com.au, Company ABN - 73 215 904 386,

Font styles to use
Sans Serif

Colors
0054AA
0677BA
7BADD7
CADEEF
E8F1F8

```html
<!DOCTYPE html>
<html lang="en">
<head>
<meta charset="utf-8">
<title>RVB Plumbing Services – Business Card</title>
<link rel="stylesheet" href="https://fonts.googleapis.com/css2?family=Roboto:wght@300;400;500;700&display=swap">
<style>
  :root {
    --ink: #1f252c;
    --navy-blue: #0054aa;
    --ocean-blue: #0677ba;
    --sky-blue: #7badd7;
    --mist-blue: #cadeef;
    --ice-blue: #e8f1f8;
    --drop-blue: #29a8e0;
    --paper: #ffffff;
  }
  * { box-sizing: border-box; margin: 0; padding: 0; }
  html, body {
    width: 1200px; height: 800px; overflow: hidden;
    background: var(--paper);
    font-family: "Roboto", sans-serif;
  }
  .canvas { position: relative; width: 1200px; height: 800px; }

  .card {
    position: absolute; left: 337px; width: 526px; height: 301px; overflow: hidden;
  }
  .card--front { top: 86px; background: var(--ink); }
  .card--back { top: 413px; background: var(--paper); }

  .brand {
    position: absolute; left: 0; right: 0;
    display: flex; flex-direction: column; align-items: center;
    font-weight: 300; white-space: nowrap;
  }
  .card--front .brand { top: 104px; color: var(--paper); }
  .card--front .brand-name { font-size: 34px; letter-spacing: 3px; }
  .brand-dot {
    width: 18px; height: 18px; border-radius: 50%;
    background: var(--drop-blue); margin-top: 14px;
  }
  .card--back .brand {
    top: 60px; left: 282px; right: 24px; color: var(--ink);
  }
  .card--back .brand-name { font-size: 19px; letter-spacing: 1.5px; }
  .card--back .brand-dot { width: 12px; height: 12px; margin-top: 9px; }

  .flow { position: absolute; inset: 0; width: 100%; height: 100%; }

  .person { position: absolute; left: 22px; top: 56px; color: var(--paper); }
  .person-name { font-size: 20px; font-weight: 500; line-height: 1.1; }
  .person-title { font-size: 12.5px; font-weight: 400; letter-spacing: 0.6px; margin-top: 2px; }

  .contacts {
    position: absolute; left: 22px; top: 151px; list-style: none;
    color: var(--ink); font-size: 12.5px; line-height: 1.15;
  }
  .contact { display: flex; align-items: center; margin-bottom: 7px; }
  .contact-icon { width: 11px; height: 11px; margin-right: 10px; flex: none; fill: var(--ink); }
</style>
</head>
<body>
<main class="canvas">

  <section class="card card--front" aria-label="Business card front">
    <div class="brand">
      <span class="brand-name">RVB Plumbing Services</span>
      <span class="brand-dot" aria-hidden="true"></span>
    </div>
  </section>

  <section class="card card--back" aria-label="Business card back">
    <svg class="flow" viewBox="0 0 658 376" preserveAspectRatio="none" role="img" aria-label="Decorative flowing water pattern in blue tones">
      <defs>
        <linearGradient id="flow-tone" gradientUnits="userSpaceOnUse" x1="0" y1="0" x2="100" y2="300">
          <stop offset="0" stop-color="#1f252c"/>
          <stop offset="0.2" stop-color="#0054aa"/>
          <stop offset="0.42" stop-color="#0677ba"/>
          <stop offset="0.6" stop-color="#7badd7"/>
          <stop offset="0.8" stop-color="#cadeef"/>
        </linearGradient>
      </defs>
      <path fill="url(#flow-tone)" d="M0 0H495C340 10 250 235 0 262Z"/>
      <path fill="url(#flow-tone)" transform="rotate(180 329 188)" d="M0 0H495C340 10 250 235 0 262Z"/>
    </svg>

    <div class="brand">
      <span class="brand-name">RVB Plumbing Services</span>
      <span class="brand-dot" aria-hidden="true"></span>
    </div>

    <div class="person">
      <p class="person-name">Owen Tredgold</p>
      <p class="person-title">Director</p>
    </div>

    <ul class="contacts">
      <li class="contact">
        <svg class="contact-icon" viewBox="0 0 24 24" aria-hidden="true"><path d="M6.6 10.8a15.1 15.1 0 0 0 6.6 6.6l2.2-2.2a1 1 0 0 1 1-.25 11.4 11.4 0 0 0 3.6.57 1 1 0 0 1 1 1V20a1 1 0 0 1-1 1A17 17 0 0 1 3 4a1 1 0 0 1 1-1h3.5a1 1 0 0 1 1 1c0 1.25.2 2.45.57 3.57a1 1 0 0 1-.25 1z"/></svg>
        <span>0431 862 507</span>
      </li>
      <li class="contact">
        <svg class="contact-icon" viewBox="0 0 24 24" aria-hidden="true"><path d="M12 2a7 7 0 0 0-7 7c0 5.2 7 13 7 13s7-7.8 7-13a7 7 0 0 0-7-7zm0 9.5A2.5 2.5 0 1 1 12 6.5a2.5 2.5 0 0 1 0 5z"/></svg>
        <span>Unit 4/22 Harbour Lane,<br>Botany NSW 2019.</span>
      </li>
      <li class="contact">
        <svg class="contact-icon" viewBox="0 0 24 24" aria-hidden="true"><path d="M12 2a10 10 0 1 0 5 18.7l-1-1.7A8 8 0 1 1 20 12v1a2 2 0 0 1-4 0V7h-2v1a5 5 0 1 0 .7 7.3A4 4 0 0 0 22 13v-1A10 10 0 0 0 12 2zm0 13a3 3 0 1 1 0-6 3 3 0 0 1 0 6z"/></svg>
        <span>owen@rvb-plumbing.com.au</span>
      </li>
      <li class="contact">
        <svg class="contact-icon" viewBox="0 0 24 24" aria-hidden="true"><path d="M12 2a10 10 0 1 0 0 20 10 10 0 0 0 0-20zm6.9 9h-3a15 15 0 0 0-1.3-6A8 8 0 0 1 18.9 11zM12 4.1A13 13 0 0 1 13.9 11h-3.8A13 13 0 0 1 12 4.1zM9.4 5a15 15 0 0 0-1.3 6h-3A8 8 0 0 1 9.4 5zM5.1 13h3a15 15 0 0 0 1.3 6A8 8 0 0 1 5.1 13zM12 19.9A13 13 0 0 1 10.1 13h3.8A13 13 0 0 1 12 19.9zm2.6-.9a15 15 0 0 0 1.3-6h3a8 8 0 0 1-4.3 6z"/></svg>
        <span>www.rvbplumbingservices.com.au</span>
      </li>
      <li class="contact">
        <svg class="contact-icon" viewBox="0 0 24 24" aria-hidden="true"><path d="M5 3h10l4 4v14H5zm2 2v14h10V8h-3V5zm2 6h6v2H9zm0 4h6v2H9z"/></svg>
        <span>ABN - 73 215 904 386</span>
      </li>
    </ul>
  </section>

</main>
</body>
</html>
```